Orbin Vale Systems

Our company is about IT hardwares and IT solutions. IT hardware such as PC, RAMS, storage and servers. IT solutions such as project management, BA. We are also selling new technology too.

Target Market(s)

Consumer, Small to Medium Business, Corporate

Requirements
Must have
• The business card must have the following:
• Name:
• Title:
• Contact Number:
• Email address:
• Website:
• Color: Must match the logo color upgrade

```html
<!DOCTYPE html>
<html lang="en">
<head>
<meta charset="utf-8">
<title>Orbin Vale Systems – Business Card</title>
<link rel="stylesheet" href="https://fonts.googleapis.com/css2?family=Rubik:wght@600&family=Open+Sans:wght@400&display=swap">
<style>
  :root {
    --canvas: #ffffff;
    --charcoal: #4f4843;
    --copper: #c8692f;
    --amber: #dc953c;
    --amber-light: #eba748;
    --ink-light: #fdf6ee;
  }
  html, body {
    margin: 0;
    padding: 0;
    width: 1200px;
    height: 1200px;
    overflow: hidden;
    background: var(--canvas);
  }
  .card {
    position: absolute;
    left: 160px;
    width: 824px;
    height: 494px;
    background: var(--charcoal);
    overflow: hidden;
  }
  .card--front { top: 60px; }
  .card--back { top: 630px; left: 158px; }

  .front-texture {
    position: absolute;
    left: 300px;
    top: 0;
    width: 524px;
    height: 100%;
    background: linear-gradient(90deg, rgba(220,149,60,0) 0%, rgba(200,120,55,0.35) 45%, rgba(235,167,72,0.9) 100%);
  }
  .company-name {
    position: absolute;
    margin: 0;
    font-family: "Rubik", sans-serif;
    font-weight: 600;
    color: var(--ink-light);
    white-space: nowrap;
    letter-spacing: 1px;
    transform: translateX(-50%);
  }
  .card--front .company-name {
    left: 412px;
    top: 262px;
    font-size: 48px;
  }
  .card--back .company-name {
    left: 207px;
    top: 234px;
    font-size: 31px;
  }

  .contact-panel {
    position: absolute;
    left: 414px;
    top: 0;
    width: 410px;
    height: 100%;
    background: linear-gradient(100deg, var(--copper) 0%, var(--amber) 55%, #d28a3a 100%);
  }
  .divider-tab {
    position: absolute;
    left: 398px;
    top: 224px;
    width: 32px;
    height: 192px;
  }
  .holder-name {
    position: absolute;
    left: 462px;
    top: 84px;
    margin: 0;
    font-family: "Open Sans", sans-serif;
    font-weight: 400;
    font-size: 31px;
    color: var(--ink-light);
  }
  .holder-title {
    position: absolute;
    left: 463px;
    top: 125px;
    margin: 0;
    font-family: "Open Sans", sans-serif;
    font-size: 16px;
    color: var(--ink-light);
  }
  .contact-list {
    position: absolute;
    left: 462px;
    top: 0;
    margin: 0;
    padding: 0;
    list-style: none;
    font-family: "Open Sans", sans-serif;
    font-size: 16px;
    line-height: 21px;
    color: var(--ink-light);
  }
  .contact-item {
    position: absolute;
    left: 0;
    width: 340px;
    display: flex;
    align-items: center;
  }
  .contact-item svg {
    flex: none;
    width: 38px;
    height: 38px;
    margin-right: 13px;
  }
  .contact-item--address { top: 227px; }
  .contact-item--phone { top: 281px; }
  .contact-item--email { top: 330px; }
  .contact-item--web { top: 374px; }
</style>
</head>
<body>

<section class="card card--front" aria-label="Card front">
  <div class="front-texture" role="img" aria-label="Geometric triangle texture fading from charcoal to amber"></div>
  <h1 class="company-name">ORBIN VALE SYSTEMS</h1>
</section>

<section class="card card--back" aria-label="Card back">
  <h2 class="company-name">ORBIN VALE SYSTEMS</h2>

  <div class="contact-panel"></div>

  <svg class="divider-tab" viewBox="0 0 32 192" aria-hidden="true">
    <rect x="0" y="0" width="22" height="192" rx="6" fill="#d07a34"/>
    <rect x="18" y="4" width="14" height="184" fill="#4f4843"/>
  </svg>

  <p class="holder-name">Mara</p>
  <p class="holder-title">Title</p>

  <ul class="contact-list">
    <li class="contact-item contact-item--address">
      <svg viewBox="0 0 38 38" aria-hidden="true">
        <path d="M19 4c-6.5 0-11 4.6-11 10.6C8 22 19 34 19 34s11-12 11-19.4C30 8.6 25.5 4 19 4z" fill="#4f4843"/>
        <circle cx="19" cy="14.5" r="4" fill="#dc953c"/>
      </svg>
      <span>PO Box 000000<br>Address</span>
    </li>
    <li class="contact-item contact-item--phone">
      <svg viewBox="0 0 38 38" aria-hidden="true">
        <circle cx="19" cy="19" r="17" fill="none" stroke="#4f4843" stroke-width="2.5"/>
        <path d="M13 10c1.5-1 3-.8 3.7.4l1.6 3c.5 1 .2 2-.7 2.6l-1.3.8c.9 2.6 2.6 4.6 5 6l1-1.2c.7-.8 1.8-.9 2.6-.3l2.8 2c1.1.8 1.1 2.3.1 3.6-1.4 1.7-3.6 2.1-5.7 1.1-5.2-2.5-8.8-6.8-10.4-12.2-.6-2.1 0-4.3 1.3-5.8z" fill="#4f4843"/>
      </svg>
      <span>000 000 000</span>
    </li>
    <li class="contact-item contact-item--email">
      <svg viewBox="0 0 38 38" aria-hidden="true">
        <rect x="3" y="9" width="32" height="21" fill="none" stroke="#4f4843" stroke-width="2.5"/>
        <path d="M3 9l16 12 16-12M3 30l12-10M35 30L23 20" fill="none" stroke="#4f4843" stroke-width="2.5"/>
      </svg>
      <span>mara@orbinvalesystems.com</span>
    </li>
    <li class="contact-item contact-item--web">
      <svg viewBox="0 0 38 38" aria-hidden="true">
        <circle cx="19" cy="19" r="16" fill="none" stroke="#4f4843" stroke-width="2.5"/>
        <ellipse cx="19" cy="19" rx="7" ry="16" fill="none" stroke="#4f4843" stroke-width="2"/>
        <path d="M4 13h30M4 25h30" stroke="#4f4843" stroke-width="2"/>
      </svg>
      <span>www.orbinvalesystems.com</span>
    </li>
  </ul>
</section>

</body>
</html>
```